Business cards

We need business cards for the logo that you designed for our company. Something simple and clean.

Target Market(s)

Homeowners/ people looking for construction work

Industry/Entity Type

Construction

Contact Information for Business Card

Name: Dana Holbrit, Number: 602-547-9164, Email: HolbritBuildingGroup@mailvesta.com ROC# 846203

Font styles to use
Serif

Colors

Designer to choose colors to be used in the design.

Requirements
Must have
• On one side of the card I would like to be all of the personal information I have put above along with the company logo that I have attached.
• On the other side of the card I would like the top half of the card to be the logo and then on the bottom half I would like to have the areas of construction we focus on along with an icon that represents it like the picture I have attached.
• Areas we focus on:
• Roofing, Kitchen and bath Remodel, Water Damage, Storm Damage, Fire Damage, Insurance Specialist
• If we could arrange those in alphabetical order.
Nice to have
• I have added 2 company logos a colorful one and a black one it would be nice to see a couple different options the black logo to be more simple and sleek and the colorful logo to be more colorful

```html
<!DOCTYPE html>
<html lang="en">
<head>
<meta charset="utf-8">
<title>Holbrit Building Group – Business Cards</title>
<link href="https://fonts.googleapis.com/css2?family=Tinos:wght@400;700&family=Lato:wght@400;700&family=Montserrat:wght@600;700&display=swap" rel="stylesheet">
<style>
  :root{
    --bg:#3b3b3b;
    --card:#ffffff;
    --blue:#33a3d8;
    --red:#e8262a;
    --green:#3f9a3c;
    --pin:#6aa843;
    --ink:#1d1d1d;
    --faint-blue:#e9f1fa;
    --faint-red:#fde8e2;
  }
  *{margin:0;padding:0;box-sizing:border-box}
  html,body{width:1200px;height:750px;overflow:hidden;background:var(--bg)}
  .stage{position:relative;width:1200px;height:750px}
  .card{position:absolute;left:367px;width:466px;height:266px;background:var(--card);overflow:hidden}
  .card--front{top:93px}
  .card--back{top:406px}

  .brand{display:flex;align-items:center;gap:10px;font-family:"Tinos",serif;font-weight:700;color:var(--blue);font-size:28px;letter-spacing:.5px;white-space:nowrap}
  .brand__mark{width:18px;height:18px;background:var(--red)}
  .card--front .brand{position:absolute;top:42px;left:0;right:0;justify-content:center}
  .card--back .brand{position:absolute;top:54px;left:24px;font-size:26px}

  .services{position:absolute;top:117px;left:0;width:100%;height:75px}
  .service{position:absolute;width:90px;margin-left:-45px;text-align:center;font-family:"Montserrat",sans-serif;color:var(--ink)}
  .service svg{display:block;margin:0 auto 4px}
  .service__main{font-size:9.5px;font-weight:700;line-height:11px}
  .service__sub{font-size:7.5px;font-weight:600;line-height:9px}
  .service-underline{position:absolute;left:109px;top:184px;width:74px;height:2px;background:var(--green)}

  .focus-list{position:absolute;top:211px;left:0;right:0;text-align:center;font-family:"Tinos",serif;font-size:12.3px;line-height:15px;color:var(--ink)}
  .front-bar{position:absolute;left:0;bottom:0;width:100%;height:8px;display:flex}
  .front-bar span:first-child{flex:0 0 232px;background:var(--red)}
  .front-bar span:last-child{flex:1;background:var(--blue)}

  .watermark-area{position:absolute;left:309px;top:3px;width:157px;height:192px;background:linear-gradient(90deg,var(--faint-blue),var(--faint-red))}

  .person{position:absolute;left:24px;top:164px}
  .person__name{font-family:"Lato",sans-serif;font-weight:700;color:var(--blue);font-size:14.5px;line-height:16px}
  .person__title{font-family:"Tinos",serif;font-size:11.5px;line-height:12px;color:var(--ink)}
  .divider{position:absolute;left:24px;top:195px;width:416px;height:1px;background:var(--red)}
  .contact{position:absolute;left:24px;top:203px;font-family:"Tinos",serif;font-size:11.5px;color:var(--ink);line-height:14.5px}
  .contact__row{display:flex;align-items:center;gap:7px}
  .contact__row svg{flex:none}
  .licence{position:absolute;right:27px;top:218px;font-family:"Tinos",serif;font-size:11.5px;color:var(--ink)}
  .back-stripes{position:absolute;left:0;bottom:0}
</style>
</head>
<body>
<div class="stage">

  <section class="card card--front">
    <div class="brand"><span class="brand__mark"></span>Holbrit Building Group</div>

    <div class="services">
      <div class="service" style="left:75px">
        <svg width="34" height="42" viewBox="0 0 34 42"><path d="M17 41C8 30 1 24 1 16A16 16 0 0 1 33 16C33 24 26 30 17 41Z" fill="var(--pin)"/><circle cx="17" cy="16" r="11" fill="#fff"/><path d="M17 8C14 13 12 15 12 18A5 5 0 0 0 22 18C22 15 20 13 17 8Z" fill="#3d6fc2"/></svg>
        <div class="service__main">WATER</div><div class="service__sub">DAMAGE</div>
      </div>
      <div class="service" style="left:146px">
        <svg width="34" height="42" viewBox="0 0 34 42"><path d="M17 41C8 30 1 24 1 16A16 16 0 0 1 33 16C33 24 26 30 17 41Z" fill="var(--pin)"/><circle cx="17" cy="16" r="11" fill="#fff"/><path d="M17 7C20 12 23 14 23 18A6 6 0 0 1 11 18C11 14 14 12 17 7Z" fill="var(--red)"/></svg>
        <div class="service__main">FIRE</div><div class="service__sub">DAMAGE</div>
      </div>
      <div class="service" style="left:223px">
        <svg width="34" height="42" viewBox="0 0 34 42"><path d="M17 41C8 30 1 24 1 16A16 16 0 0 1 33 16C33 24 26 30 17 41Z" fill="var(--pin)"/><circle cx="17" cy="16" r="11" fill="#fff"/><circle cx="17" cy="16" r="6" fill="#3d7f2f"/></svg>
        <div class="service__main">MOLD</div><div class="service__sub">REMEDIATION</div>
      </div>
      <div class="service" style="left:300px">
        <svg width="34" height="42" viewBox="0 0 34 42"><path d="M17 41C8 30 1 24 1 16A16 16 0 0 1 33 16C33 24 26 30 17 41Z" fill="var(--pin)"/><circle cx="17" cy="16" r="11" fill="#fff"/><ellipse cx="17" cy="15" rx="7" ry="4.5" fill="#4f5a86"/></svg>
        <div class="service__main">STORM</div><div class="service__sub">DAMAGE</div>
      </div>
      <div class="service" style="left:377px">
        <svg width="34" height="42" viewBox="0 0 34 42"><path d="M17 41C8 30 1 24 1 16A16 16 0 0 1 33 16C33 24 26 30 17 41Z" fill="var(--pin)"/><circle cx="17" cy="16" r="11" fill="#fff"/><rect x="10" y="10" width="14" height="12" fill="#f08a2a"/></svg>
        <div class="service__main">COMMERCIAL</div><div class="service__sub">SERVICES</div>
      </div>
    </div>
    <div class="service-underline"></div>

    <p class="focus-list">Roofing | Kitchen and bath Remodel | Water Damage | Storm Damage<br>Fire Damage | Insurance Specialist</p>

    <div class="front-bar"><span></span><span></span></div>
  </section>

  <section class="card card--back">
    <div class="watermark-area" role="img" aria-label="Large faint company mark in soft blue and red"></div>
    <div class="brand"><span class="brand__mark"></span>Holbrit Building Group</div>

    <div class="person">
      <div class="person__name">Dana Holbrit</div>
      <div class="person__title">Executive Assistant</div>
    </div>
    <div class="divider"></div>

    <div class="contact">
      <div class="contact__row">
        <svg width="9" height="11" viewBox="0 0 9 11"><rect x="1" y="1" width="7" height="9" rx="1" fill="none" stroke="var(--red)" stroke-width="1.4"/></svg>
        602-547-9164
      </div>
      <div class="contact__row">
        <svg width="10" height="8" viewBox="0 0 10 8"><rect width="10" height="8" fill="var(--red)"/><path d="M0 0L5 4.5L10 0M0 8L4 3.5M10 8L6 3.5" stroke="#fff" stroke-width=".9" fill="none"/></svg>
        HolbritBuildingGroup@mailvesta.com
      </div>
    </div>
    <div class="licence">ROC# 846203</div>

    <svg class="back-stripes" width="466" height="24" viewBox="0 0 466 24">
      <rect x="0" y="4" width="293" height="5" fill="#111"/>
      <path d="M293 0H466V24H286Z" fill="var(--blue)"/>
      <rect x="0" y="16" width="466" height="8" fill="var(--blue)"/>
    </svg>
  </section>

</div>
</body>
</html>
```